COMMERCIAL OFFICE FOR SALE- Brochure, Miami, FL 33131

BROCHURE DESIGN BRIEF – COMMERCIAL OFFICE FOR SALE

I need a clean, modern brochure for a commercial office listing (FOR SALE, not lease). This will be used both digitally (email + SpanDesk/attachments) and printed if needed.

Please follow a “Sample Flyer Copy” style layout — strong headline, clean sections, minimal clutter, and easy to scan. Use fints Seasons and Poppins interchangeably.

All property details, specs, and exact wording should be pulled directly from the MLS Listing file I provided. Do not guess or rewrite specs.

OVERALL LOOK + FEEL

Clean, high-end, professional (Brickell / financial district vibe)

Think: simple, sharp, not busy

Neutral palette (white, black, soft gray) + subtle accent color if needed

Prioritize readability over design gimmicks

Plenty of white space

FORMAT

1-page flyer (primary)

Also format so it can easily convert into a 2-page version if needed

PDF optimized for email + print

HEADER SECTION (TOP OF PAGE)

Large, strong headline:

Example: “Office Condo for Sale | Brickell” (adjust based on MLS info)

Subheadline (smaller):

Key positioning (corner unit, square footage, etc.)

Include 1 strong hero image (best photo of the unit)

PROPERTY OVERVIEW (RIGHT UNDER HEADER OR NEXT BLOCK)

Clean bullet section with icons if possible:

Include:

Total square footage

Layout highlights (conference room, offices, open workspace, etc.)

Kitchen / breakroom

Reception area

Storage / printer room

Floor or suite number

Any standout feature (corner unit, natural light, views, etc.)

Keep this tight and clean — no long paragraphs.

PRICING SECTION

Clearly state: FOR SALE

Price (from MLS)

Price per square foot

Make this visually stand out.

LOCATION SECTION

Short and clean:

Building name + address

1–2 lines max on location advantages (Brickell, access, etc.)

Optional small map if it fits cleanly

ADDITIONAL DETAILS (IF SPACE ALLOWS)

Building amenities (if relevant)

Parking info

Zoning / permitted uses (if applicable)

Only include what is confirmed in MLS.

IMAGES

3–5 total max

Keep it clean — do not overcrowd

Prioritize:

Main workspace

Conference room

Kitchen

Any standout feature

CONTACT SECTION (VERY IMPORTANT – EXACT FORMAT)

This must be clean and prominent.

Colette Varnum
REALTOR®
Tamsworth Lindale HomePartners QRF Realty

Phone: [your number]
Email: [your email]

Call to action line:

“For more information or to schedule a private showing, contact Colette Varnum.”

Include my business card details (office location etc.) in this section.

BROKERAGE + LOGOS

Use TLHP QRF Realty logos provided

Place cleanly (bottom or footer)

Do not distort or restyle logos

FOOTER

Standard disclaimer if needed

Keep minimal

IMPORTANT NOTES

This is a SALE listing — do not use the word lease anywhere

Do not overdesign — clean always wins

Keep everything aligned and balanced

Make sure spacing feels high-end, not cramped
Updates

Please include this video link within the document: https://vidshare.example/kQ7pTzR2vNa?ref=hx4Lm9Ys_Wd2Pc8E

State: Step inside. Watch the full video tour. and hyperlink Watch with the link

Target Market(s)

Buyers, Professionals, Lawyer Office, Family Office, Small FInancial Offices

Industry/Entity Type

Commercial Real Estate

Font styles to use
Serif
Sans Serif

Requirements
Must have
• Clean, clear, layout and good imagery
Should not have
• Professional flow, follow my font guidlines and thebrochure i shared as a guide

```html
<!DOCTYPE html>
<html lang="en">
<head>
<meta charset="utf-8">
<title>Office Condo For Sale</title>
<link rel="stylesheet" href="https://fonts.googleapis.com/css2?family=Montserrat:wght@400;500;600;700;800;900&family=Kaushan+Script&display=swap">
<style>
  :root {
    --backdrop: #bcbdbf;
    --paper: #ffffff;
    --ink: #000000;
    --text: #1a1a1a;
    --price-bg: #efedea;
    --rule: #222222;
  }
  * { margin: 0; padding: 0; box-sizing: border-box; }
  html, body { width: 1200px; height: 1200px; overflow: hidden; background: var(--backdrop); }
  body { font-family: "Montserrat", sans-serif; color: var(--text); position: relative; }
  .flyer { position: absolute; left: 243px; top: 95px; width: 713px; height: 1009px; background: var(--paper); overflow: hidden; }
  .abs { position: absolute; }

  .headline-top { left: 33px; top: 38px; font-weight: 900; font-size: 68px; line-height: 1; letter-spacing: 0.2px; color: var(--ink); white-space: nowrap; }
  .headline-for { left: 38px; top: 104px; font-family: "Kaushan Script", cursive; font-size: 66px; line-height: 1.2; color: var(--ink); }
  .headline-sale { left: 146px; top: 107px; font-weight: 800; font-size: 102px; line-height: 1; color: var(--ink); letter-spacing: -1px; }

  .photo { position: absolute; }
  .photo-hero { left: 33px; top: 238px; width: 280px; height: 187px; background: linear-gradient(180deg, #6aa0d8 0%, #9cc4e8 40%, #7e8c6a 75%, #5a4a3a 100%); }
  .photo-tower { left: 326px; top: 238px; width: 139px; height: 187px; background: linear-gradient(160deg, #4f86c9 0%, #2e5e9a 55%, #3f6b46 100%); }
  .photo-office { left: 325px; top: 436px; width: 142px; height: 146px; background: linear-gradient(180deg, #e8e6e2 0%, #d9d6d0 55%, #7b7d84 100%); }
  .photo-kitchen { left: 325px; top: 592px; width: 142px; height: 145px; background: linear-gradient(180deg, #d8c9ac 0%, #ece8e0 55%, #f1efec 100%); }
  .photo-map { left: 487px; top: 538px; width: 194px; height: 199px; background: linear-gradient(135deg, #f2f1ee 0%, #ebe6d8 60%, #e8e9ec 100%); }
  .photo-agent { left: 487px; top: 768px; width: 194px; height: 147px; background: linear-gradient(180deg, #e4ded4 0%, #d9d2c6 100%); }

  .price-box { left: 487px; top: 238px; width: 194px; height: 91px; background: var(--price-bg); text-align: center; }
  .price-label { margin-top: 7px; font-size: 15px; font-weight: 500; }
  .price-value { font-size: 29px; font-weight: 800; line-height: 1.2; color: var(--ink); }
  .price-psf { font-size: 15px; font-weight: 500; margin-top: 1px; }

  .section-title { font-weight: 700; font-size: 15px; color: var(--ink); border-bottom: 1px solid var(--rule); line-height: 1.2; }
  .overview-title { left: 33px; top: 446px; width: 195px; }
  .location-title { left: 486px; top: 349px; width: 196px; }

  .bullets { list-style: none; font-size: 11px; font-weight: 500; }
  .bullets li { position: relative; padding-left: 15px; height: 19.5px; line-height: 19.5px; white-space: nowrap; }
  .bullets li::before { content: ""; position: absolute; left: 2px; top: 7.5px; width: 5px; height: 5px; border-radius: 50%; background: var(--ink); }
  .overview-list { left: 33px; top: 469px; }
  .location-list { left: 487px; top: 442px; }

  .building-name { left: 486px; top: 367px; font-weight: 700; font-size: 15.5px; color: var(--ink); white-space: nowrap; }
  .building-address { left: 487px; top: 390px; font-size: 12px; font-weight: 500; line-height: 17px; white-space: nowrap; }

  .video-tour { left: 33px; top: 655px; width: 280px; height: 82px; background: var(--price-bg); display: flex; align-items: center; gap: 12px; padding: 0 16px; }
  .video-tour .play { flex: none; }
  .video-text { font-size: 12.3px; font-weight: 500; line-height: 18px; color: var(--text); }
  .video-text strong { display: block; font-size: 15px; font-weight: 700; color: var(--ink); }
  .video-text a { color: var(--ink); font-weight: 700; text-decoration: underline; }

  .agent-name { left: 33px; top: 763px; font-weight: 700; font-size: 23px; color: var(--ink); white-space: nowrap; }
  .agent-name small { font-size: 11.5px; font-weight: 500; letter-spacing: 0.3px; }
  .agent-company { left: 33px; top: 792px; font-size: 12.3px; font-weight: 500; white-space: nowrap; }
  .agent-phone { left: 55px; top: 823px; font-weight: 800; font-size: 21px; color: var(--ink); white-space: nowrap; }
  .agent-web { left: 56px; top: 853px; font-weight: 600; font-size: 13px; line-height: 17px; color: var(--ink); }
  .icon { position: absolute; }
  .cta { left: 33px; top: 899px; font-size: 12.3px; font-weight: 500; line-height: 17px; }
  .cta strong { font-weight: 700; color: var(--ink); }
  .footer-rule { left: 33px; top: 947px; width: 447px; height: 1px; background: var(--rule); }
  .office-address { left: 56px; top: 959px; font-size: 13px; font-weight: 500; white-space: nowrap; }

  .brokerage-name { left: 491px; top: 930px; font-weight: 700; font-size: 17px; line-height: 19px; color: var(--ink); letter-spacing: 0.5px; }
</style>
</head>
<body>
  <main class="flyer">
    <h1>
      <span class="abs headline-top">OFFICE CONDO</span>
      <span class="abs headline-for">For</span>
      <span class="abs headline-sale">SALE</span>
    </h1>

    <div class="photo photo-hero" role="img" aria-label="Office window view over the Brickell skyline and park"></div>
    <div class="photo photo-tower" role="img" aria-label="Glass office tower exterior with palm trees"></div>
    <div class="photo photo-office" role="img" aria-label="Private corner office with windows and desk"></div>
    <div class="photo photo-kitchen" role="img" aria-label="Kitchen and breakroom with wood cabinets"></div>
    <div class="photo photo-map" role="img" aria-label="Street map showing the office tower location"></div>
    <div class="photo photo-agent" role="img" aria-label="Portrait of the realtor"></div>

    <section class="abs price-box">
      <p class="price-label">For Sale</p>
      <p class="price-value">$ 2,250,000</p>
      <p class="price-psf">$789 / SF</p>
    </section>

    <h2 class="abs section-title overview-title">PROPERTY OVERVIEW</h2>
    <ul class="abs bullets overview-list">
      <li>2,850 SF Corner Unit</li>
      <li>4 Private Glass Offices</li>
      <li>Large Open Workspace</li>
      <li>Conference Room</li>
      <li>Modern Kitchen/ Breakroom</li>
      <li>Reception Area</li>
      <li>Storage / Printer Room</li>
      <li>Stunning City Views</li>
    </ul>

    <section class="abs video-tour">
      <svg class="play" width="34" height="34" viewBox="0 0 34 34" aria-hidden="true">
        <circle cx="17" cy="17" r="16" fill="none" stroke="#000" stroke-width="2"/>
        <path d="M13.5 10.5v13l10.5-6.5z" fill="#000"/>
      </svg>
      <p class="video-text"><strong>Step inside.</strong><a href="https://vidshare.example/kQ7pTzR2vNa?ref=hx4Lm9Ys_Wd2Pc8E">Watch</a> the full video tour.</p>
    </section>

    <h2 class="abs section-title location-title">LOCATION</h2>
    <p class="abs building-name">Baywater Office Tower</p>
    <p class="abs building-address">2150 Baywater Drive, Suit 1502<br>Miami, Fl 33131</p>
    <ul class="abs bullets location-list">
      <li>Prime Brickell Location</li>
      <li>Easy Access to I-95</li>
      <li>Walk to Dining, Shop, Metrorail</li>
    </ul>

    <p class="abs agent-name">Colette Varnum <small>REALTOR®</small></p>
    <p class="abs agent-company">Tamsworth Lindale HomePartners QRF Realty</p>

    <svg class="icon" style="left:31px;top:827px" width="17" height="17" viewBox="0 0 24 24" aria-hidden="true">
      <path d="M6.6 10.8a15 15 0 0 0 6.6 6.6l2.2-2.2a1 1 0 0 1 1-.25 11.4 11.4 0 0 0 3.6.57 1 1 0 0 1 1 1V20a1 1 0 0 1-1 1A17 17 0 0 1 3 4a1 1 0 0 1 1-1h3.5a1 1 0 0 1 1 1c0 1.250.2 2.45.57 3.6a1 1 0 0 1-.25 1z" fill="#000"/>
      <path d="M14 3a7 7 0 0 1 7 7M14 6.5a3.5 3.5 0 0 1 3.5 3.5" stroke="#000" stroke-width="1.8" fill="none"/>
    </svg>
    <p class="abs agent-phone">555 014 2876</p>

    <svg class="icon" style="left:30px;top:858px" width="19" height="17" viewBox="0 0 24 22" aria-hidden="true">
      <path d="M23 1 1 9l8 3 2 8 4-6 6 4z M9 12 23 1" fill="#000" stroke="#000" stroke-width="1" stroke-linejoin="round"/>
    </svg>
    <p class="abs agent-web">colettevarnum@mailbox.example<br>colettevarnum.qrf.example</p>

    <p class="abs cta">For more information or to schedule a private showing,<br>contact <strong>Colette Varnum.</strong></p>

    <div class="abs footer-rule"></div>
    <svg class="icon" style="left:34px;top:960px" width="13" height="15" viewBox="0 0 16 20" aria-hidden="true">
      <path d="M8 1a6 6 0 0 0-6 6c0 4.5 6 10 6 10s6-5.5 6-10a6 6 0 0 0-6-6z" fill="none" stroke="#000" stroke-width="1.8"/>
      <circle cx="8" cy="7" r="2" fill="#000"/>
      <path d="M2 19h12" stroke="#000" stroke-width="1.8"/>
    </svg>
    <p class="abs office-address">410 Harbor Crest Avenue, Coral Gables, FL 33146</p>

    <p class="abs brokerage-name">TLHP QRF<br>REALTY</p>
  </main>
</body>
</html>
```